Energieausweis
Zielgruppe
Zielgruppe sind Immobilieninteressenten - Verwendung in einem Immobilienmagazin und im Internet.
Aufgabenstellung
Ab dem 1. Mai muss in Deutschland die Energie-Effizienzklasse bei Immobilienangeboten mit veröffentlicht werden. Das kann man nüchtern in Zahlen darstellen, aber auch in einer netten Grafik. In der Anlage finden 2 von uns gekaufte Pixbarun-Bilder. Das Bild mit dem Männchen ist eine sehr nette Idee. Da wir in unserem Logo auch ein Männchen haben, bietet es sich an, ein LindenHaus-Männchen zusammen mit der bunten Grafik zu gestalten. (Das Pixbarun-Bild soll nur die Idee erklären - bitte nicht verwenden). Wenn die Grafik fertig ist, legen wir einen Pfeil zur Kennzeichnung der jeweiligen Energieklasse hinzu. Das heisst, wir haben dann für jede Energieklasse eine entsprechende Vorlage und dem richtig platzierten Pfeil. Weiter finden sie in der Anlage unser Firmenlogo zur freuen Verwendung.

```html
<!DOCTYPE html>
<html lang="de">
<head>
<meta charset="utf-8">
<title>Energieausweis – LindenHaus</title>
<link rel="stylesheet" href="https://fonts.googleapis.com/css2?family=Cabin:wght@600;700&family=Source+Code+Pro:wght@300;400;600&display=swap">
<style>
  :root {
    --brand-blue: #0f4f8f;
    --ink: #111;
    --white: #fff;
    --class-a: #076a2f;
    --class-b: #229b2a;
    --class-c: #9fbc08;
    --class-d: #e0da0e;
    --class-e: #ecb903;
    --class-f: #e97203;
    --class-g: #e01f22;
    --marker: #030a05;
  }
  html, body {
    margin: 0;
    padding: 0;
    width: 719px;
    height: 1200px;
    overflow: hidden;
    background: var(--white);
  }
  .certificate {
    position: relative;
    width: 719px;
    height: 1200px;
  }
  .certificate__frame {
    position: absolute;
    left: 17px;
    top: 29px;
    width: 670px;
    height: 1125px;
    border: 8.5px solid var(--brand-blue);
    border-radius: 22px;
  }
  .certificate__title {
    position: absolute;
    margin: 0;
    left: 74px;
    top: 63px;
    width: 572px;
    height: 102px;
    background: var(--brand-blue);
    color: var(--white);
    font-family: "Cabin", sans-serif;
    font-weight: 700;
    font-size: 67px;
    letter-spacing: -3px;
    line-height: 102px;
    text-align: center;
  }
  .facts {
    font-family: "Source Code Pro", monospace;
    color: var(--ink);
    position: absolute;
    left: 0;
    top: 0;
  }
  .facts span { position: absolute; white-space: nowrap; line-height: 1; }
  .facts .label { font-weight: 600; font-size: 19px; }
  .facts .value { font-weight: 300; font-size: 18px; top: inherit; }
  .scale {
    position: absolute;
    left: 0;
    top: 0;
  }
  .scale text {
    font-family: "Cabin", sans-serif;
    font-weight: 700;
    font-size: 52px;
    fill: var(--white);
  }
  .stat {
    position: absolute;
    top: 1022px;
    height: 71px;
    border-radius: 10px;
    box-sizing: border-box;
    display: flex;
    flex-direction: column;
    align-items: center;
    justify-content: center;
    font-family: "Cabin", sans-serif;
    font-weight: 700;
    font-size: 21px;
    line-height: 1.15;
    text-align: center;
  }
  .stat--rooms {
    left: 51px;
    width: 143px;
    background: var(--brand-blue);
    color: var(--white);
  }
  .stat--area {
    left: 238px;
    width: 141px;
    border: 5px solid var(--brand-blue);
    color: var(--ink);
  }
  .brand {
    position: absolute;
    left: 425px;
    top: 1040px;
    display: flex;
    align-items: center;
    gap: 12px;
  }
  .brand__dot {
    width: 30px;
    height: 30px;
    border-radius: 50%;
    background: var(--brand-blue);
  }
  .brand__name {
    font-family: "Cabin", sans-serif;
    font-weight: 700;
    font-size: 32px;
    color: var(--brand-blue);
  }
</style>
</head>
<body>
<main class="certificate">
  <div class="certificate__frame"></div>
  <h1 class="certificate__title">ENERGIEAUSWEIS</h1>

  <div class="facts">
    <span class="label" style="left:74px;top:184px">Gebäudeart</span>
    <span class="value" style="left:203px;top:185px">Mehrfamilienhaus</span>
    <span class="label" style="left:411px;top:184px">Baujahr Gebäude</span>
    <span class="value" style="left:596px;top:185px">1996</span>

    <span class="label" style="left:74px;top:235px">Straße</span>
    <span class="value" style="left:203px;top:236px">Musterweg 2d</span>
    <span class="label" style="left:411px;top:235px">Baujahr Anlage</span>
    <span class="value" style="left:596px;top:236px">2001</span>

    <span class="label" style="left:74px;top:260px">PLZ/Ort</span>
    <span class="value" style="left:203px;top:261px">56789 Musterstadt</span>
    <span class="label" style="left:411px;top:260px">Energieträger</span>
    <span class="value" style="left:596px;top:261px">Erdöl</span>
  </div>

  <svg class="scale" width="719" height="1000" viewBox="0 0 719 1000" aria-label="Energieeffizienzklassen A bis G, Klasse B markiert">
    <g stroke-linejoin="round" stroke-width="3">
      <polygon fill="var(--class-a)" stroke="var(--class-a)" points="49,334 247,334 273,373 247,412 49,412"/>
      <polygon fill="var(--class-b)" stroke="var(--class-b)" points="49,429 273,429 302,468 273,507 49,507"/>
      <polygon fill="var(--class-c)" stroke="var(--class-c)" points="49,524 303,524 334,563 303,602 49,602"/>
      <polygon fill="var(--class-d)" stroke="var(--class-d)" points="49,619 334,619 370,658 334,697 49,697"/>
      <polygon fill="var(--class-e)" stroke="var(--class-e)" points="49,714 371,714 411,753 371,792 49,792"/>
      <polygon fill="var(--class-f)" stroke="var(--class-f)" points="52,809 415,809 459,848 415,887 52,887"/>
      <polygon fill="var(--class-g)" stroke="var(--class-g)" points="49,904 458,904 509,943 458,982 49,982"/>
      <polygon fill="var(--marker)" stroke="var(--marker)" points="451,429 517,429 517,507 451,507 426,468"/>
    </g>
    <text x="57" y="392">A</text>
    <text x="60" y="487">B</text>
    <text x="58" y="582">C</text>
    <text x="58" y="677">D</text>
    <text x="62" y="772">E</text>
    <text x="64" y="867">F</text>
    <text x="57" y="962">G</text>
    <text x="459" y="487">B</text>
  </svg>

  <div class="stat stat--rooms"><span>5</span><span>Räume</span></div>
  <div class="stat stat--area"><span>110</span><span>m²</span></div>

  <div class="brand">
    <div class="brand__dot"></div>
    <div class="brand__name">LindenHaus</div>
  </div>
</main>
</body>
</html>
```